Hi, Looking for an upgraded business card to the aged one attached. Open to suggestions and no real limitations, but if your going to use a picture of a taxi i think it should be vector based rather than a full color picture. I've uploaded a 2 pictures of the type of taxi which is a Torvane K5 in white. The taxi markings look like the pink one in the picture but to be clear his is white. The taxi is in Bermuda so if you wanted to include something island based that's ok as well but not required. The other thing he wanted to keep on there was the bermuda police crest, with the retired police office incorporated somehow.

Requirements
Must have
• Bermuda Taxi Operator
Retired Police Officer
Police Crest
Taxi #
Email
Mobile Number

```html
<!DOCTYPE html>
<html lang="en">
<head>
<meta charset="utf-8">
<title>Bermuda Taxi Operator – Business Card</title>
<link rel="stylesheet" href="https://fonts.googleapis.com/css2?family=Oswald:wght@500;600&family=Montserrat:wght@500;600&display=swap">
<style>
  :root{
    --navy:#0d4a94;
    --ink:#2f2f2f;
    --white:#ffffff;
    --stage:#e9ebee;
    --sky:#8fc3ea;
    --sea:#5fd0cf;
    --sand:#efe6d4;
    --van:#d9dadc;
  }
  *{margin:0;padding:0;box-sizing:border-box}
  html,body{width:1200px;height:1015px;overflow:hidden;background:var(--stage)}
  .canvas{position:relative;width:1200px;height:1015px}
  .card{position:absolute;left:215px;width:770px;height:440px;overflow:hidden;background:var(--white);box-shadow:0 6px 18px rgba(0,0,0,.18)}
  .card--front{top:45px}
  .card--back{top:530px}
  .card__art{position:absolute;inset:0;width:100%;height:100%}
  .front__title{position:absolute;left:0;right:0;top:92px;text-align:center;font-family:"Oswald",sans-serif;font-weight:600;font-size:54px;letter-spacing:.5px;color:var(--navy)}
  .back__contact{position:absolute;left:45px;top:205px;color:var(--white);font-family:"Oswald",sans-serif;font-weight:500}
  .contact__phone{font-size:40px;line-height:1.1;white-space:nowrap}
  .contact__taxi{font-size:19px;letter-spacing:1px;margin:8px 0 0 70px}
  .contact__email{font-size:20px;letter-spacing:1px;margin-top:26px;white-space:nowrap}
  .back__title{position:absolute;left:392px;top:68px;font-family:"Oswald",sans-serif;font-weight:600;font-size:32px;color:var(--ink);white-space:nowrap}
  .org{position:absolute;left:408px;top:148px;width:92px;text-align:center}
  .org__mark{width:70px;height:70px;border-radius:50%;border:4px solid var(--navy);margin:0 auto}
  .org__name{font-family:"Montserrat",sans-serif;font-weight:600;font-size:9px;color:var(--navy);margin-top:5px;letter-spacing:.3px}
  .person{position:absolute;left:508px;top:160px;font-family:"Montserrat",sans-serif;color:var(--ink);white-space:nowrap}
  .person__name{font-weight:600;font-size:22px;letter-spacing:.5px}
  .person__role{font-weight:500;font-size:15px;margin-top:2px}
  .back__van{position:absolute;left:525px;top:270px;width:205px;height:100px}
</style>
</head>
<body>
<main class="canvas">
  <section class="card card--front">
    <svg class="card__art" viewBox="0 0 770 440" role="img" aria-label="Beach photograph with turquoise sea, white sand, green plants and two white taxi vans">
      <defs>
        <linearGradient id="beach" x1="0" y1="0" x2="0" y2="1">
          <stop offset="0" stop-color="var(--sky)"/>
          <stop offset=".35" stop-color="#d8ecf6"/>
          <stop offset=".45" stop-color="var(--sea)"/>
          <stop offset=".62" stop-color="var(--sand)"/>
          <stop offset="1" stop-color="#e4d9c3"/>
        </linearGradient>
      </defs>
      <rect width="770" height="440" fill="url(#beach)"/>
    </svg>
    <div class="front__title">BERMUDA TAXI OPERATOR</div>
  </section>

  <section class="card card--back">
    <svg class="card__art" viewBox="0 0 770 440" aria-hidden="true">
      <rect width="770" height="440" fill="var(--navy)"/>
      <circle cx="640" cy="120" r="292" fill="var(--white)"/>
      <circle cx="640" cy="120" r="280" fill="none" stroke="var(--navy)" stroke-width="4"/>
    </svg>
    <div class="back__contact">
      <div class="contact__phone">1-441-555-0182</div>
      <div class="contact__taxi">TAXI# T2718</div>
      <div class="contact__email">DSALT214@POSTMAIL.COM</div>
    </div>
    <div class="back__title">BERMUDA TAXI OPERATOR</div>
    <div class="org">
      <div class="org__mark"></div>
      <div class="org__name">HARBOUR CONSTABULARY</div>
    </div>
    <div class="person">
      <div class="person__name">DORIAN SALTMARSH</div>
      <div class="person__role">Retired Police Officer</div>
    </div>
    <svg class="back__van" viewBox="0 0 205 100" role="img" aria-label="Vector illustration of a white Torvane K5 taxi van">
      <rect width="205" height="100" rx="14" fill="var(--van)"/>
    </svg>
  </section>
</main>
</body>
</html>
```